Business Card for Makeup Artist

I need a business card designed for my makeup and hair artistry business which is primarily events and weddings focused. The card needs to be sleek, simple, stylish and appealing to women. I would prefer a white background but open to suggestions also. I also love the marble background look. I have attached some example pics. It needs to be a double sided card with logo and/or design on one side and contact details in the centre of the card on the other side. NO LOGO ON BACK. Examples attached.

Target Market(s)

Females age 14-55

Industry/Entity Type

Business

Contact Information for Business Card

Nora Vint
Principal Makeup Artist
P: 0413 925 214
E: nora@lumirabeauty.com.au
W: www.lumirabeauty.com.au

Requirements
Should not have
• No yellow, green, red or blue in the design.

```html
<!DOCTYPE html>
<html lang="en">
<head>
<meta charset="utf-8">
<title>Lumira Makeup Artistry – Business Card</title>
<link rel="stylesheet" href="https://fonts.googleapis.com/css2?family=Montserrat:wght@400;500;600&display=swap">
<style>
  :root {
    --stage: #e9e7e8;
    --card-black: #141414;
    --card-white: #ffffff;
    --ink: #3a3a3c;
    --ink-soft: #4a4a4d;
    --pink: #d64fbf;
    --pink-faint: #f7d9ef;
    --logo-white: #eeeeee;
  }
  * { margin: 0; padding: 0; box-sizing: border-box; }
  html, body {
    width: 1200px;
    height: 871px;
    overflow: hidden;
    background: var(--stage);
    font-family: "Montserrat", Arial, sans-serif;
  }
  .stage {
    position: relative;
    width: 1200px;
    height: 871px;
  }
  .card {
    position: absolute;
    width: 580px;
    height: 354px;
    border-radius: 4px;
    box-shadow: 0 10px 30px rgba(0,0,0,0.18);
    overflow: hidden;
  }

  /* Front */
  .card-front {
    left: 110px;
    top: 80px;
    background: var(--card-black);
  }
  .brand {
    position: absolute;
    left: 0;
    right: 0;
    top: 112px;
    text-align: center;
    color: var(--logo-white);
  }
  .brand-name {
    font-size: 64px;
    font-weight: 500;
    letter-spacing: 2px;
    line-height: 1;
  }
  .brand-tagline {
    margin-top: 10px;
    font-size: 17px;
    font-weight: 400;
    letter-spacing: 3px;
  }

  /* Back */
  .card-back {
    left: 520px;
    top: 410px;
    background: var(--card-white);
  }
  .watermark {
    position: absolute;
    right: -40px;
    top: -30px;
    font-size: 150px;
    font-weight: 500;
    color: var(--pink-faint);
    line-height: 1;
    letter-spacing: 4px;
  }
  .contact {
    position: absolute;
    left: 34px;
    top: 150px;
    font-size: 15px;
    line-height: 24px;
  }
  .contact-row { display: flex; gap: 16px; }
  .contact-key { color: var(--pink); font-weight: 600; width: 12px; }
  .contact-value { color: var(--ink-soft); font-weight: 400; }
  .person {
    position: absolute;
    right: 38px;
    bottom: 48px;
    text-align: left;
  }
  .person-name {
    font-size: 38px;
    font-weight: 600;
    color: var(--ink);
    line-height: 1.1;
  }
  .person-name .initial { color: var(--pink); }
  .person-title {
    font-size: 19px;
    font-weight: 500;
    color: var(--pink);
    margin-top: 2px;
  }
</style>
</head>
<body>
<main class="stage">
  <section class="card card-front" aria-label="Card front">
    <div class="brand">
      <div class="brand-name">Lumira</div>
      <div class="brand-tagline">MAKEUP ARTISTRY</div>
    </div>
  </section>

  <section class="card card-back" aria-label="Card back">
    <div class="watermark" aria-hidden="true">Lumira</div>
    <div class="contact">
      <div class="contact-row"><span class="contact-key">P</span><span class="contact-value">0413 925 214</span></div>
      <div class="contact-row"><span class="contact-key">E</span><span class="contact-value">nora@lumirabeauty.com.au</span></div>
      <div class="contact-row"><span class="contact-key">W</span><span class="contact-value">www.lumirabeauty.com.au</span></div>
    </div>
    <div class="person">
      <div class="person-name"><span class="initial">N</span>ora <span class="initial">V</span>int</div>
      <div class="person-title">Principal Makeup Artist</div>
    </div>
  </section>
</main>
</body>
</html>
```